Business Card Design

We need a business card design for a Dry cleaners in Brisbane, Australia. We are trying to promote a fresh/clean image consistent with our website. www.quillpresswash.com.au

Looking for a professional neat card that's easy to read.

Target Market(s)

Customers looking for a professional, fresh and clean drycleaners.

Industry/Entity Type

Business

Contact Information for Business Card

See our existing business card. The Fax number (07) 3468 5203 to be removed.

Requirements
Must have
• All the details on current business card less the fax number.
Nice to have
• I like white text on coloured background. Blue works well as we are located near the water...

```html
<!DOCTYPE html>
<html lang="en">
<head>
<meta charset="utf-8">
<title>Quill Press Wash – Business Card</title>
<link href="https://fonts.googleapis.com/css2?family=Open+Sans:ital,wght@0,400;0,600;0,700;1,700&display=swap" rel="stylesheet">
<style>
  :root {
    --band-blue: #223f9a;
    --brand-blue: #0a6cc0;
    --card-white: #ffffff;
    --muted-grey: #6a6a6a;
    --divider-grey: #9a9a9a;
    --edge: #c9cbe0;
    --text-white: #ffffff;
  }
  * { margin: 0; padding: 0; box-sizing: border-box; }
  html, body { width: 1200px; height: 900px; overflow: hidden; }
  body {
    background: radial-gradient(ellipse at center, #ffffff 55%, #e4e5e7 100%);
    font-family: "Open Sans", sans-serif;
    position: relative;
  }
  .business-card {
    position: absolute;
    left: 342px;
    top: 294px;
    width: 516px;
    height: 312px;
    background: var(--card-white);
    border: 1px solid var(--edge);
    display: flex;
    flex-direction: column;
  }
  .contact-band {
    height: 116px;
    background: var(--band-blue);
    color: var(--text-white);
    text-align: center;
    padding-top: 24px;
  }
  .person-name {
    font-weight: 700;
    font-style: italic;
    font-size: 22px;
    line-height: 1.1;
    margin-bottom: 4px;
  }
  .contact-line { font-size: 13.5px; line-height: 17px; }
  .brand-band {
    height: 114px;
    display: flex;
    flex-direction: column;
    align-items: center;
    justify-content: flex-end;
    gap: 14px;
    padding-bottom: 10px;
  }
  .brand-mark { display: flex; align-items: center; gap: 10px; }
  .brand-dot { width: 20px; height: 20px; border-radius: 50%; background: var(--brand-blue); }
  .brand-name { font-weight: 700; font-size: 26px; line-height: 34px; color: var(--brand-blue); letter-spacing: 0.5px; }
  .branch-list { font-weight: 600; font-size: 11px; line-height: 15px; color: var(--muted-grey); }
  .branch-list .divider { color: var(--divider-grey); font-weight: 400; padding: 0 1px; }
  .address-band {
    flex: 1;
    background: var(--band-blue);
    color: var(--text-white);
    display: flex;
    align-items: flex-end;
    justify-content: center;
    padding-bottom: 17px;
    font-size: 13.5px;
  }
</style>
</head>
<body>
  <section class="business-card">
    <div class="contact-band">
      <p class="person-name">Dana Merrick</p>
      <p class="contact-line">M: 0412 586 304</p>
      <p class="contact-line">E: dana@quillpresswash.com.au</p>
    </div>
    <div class="brand-band">
      <div class="brand-mark">
        <span class="brand-dot"></span>
        <span class="brand-name">Quill Press Wash</span>
      </div>
      <p class="branch-list">Harbury <span class="divider">|</span> Ellerton <span class="divider">|</span> Carden Pt</p>
    </div>
    <div class="address-band">
      <p>18 Marlow St Harbury Qld 4290&nbsp;&nbsp;P: (07) 3521 7746</p>
    </div>
  </section>
</body>
</html>
```